Vellum Systemics Buisness Cards

I need a technology focused clean business card for my employees. I have attached out logo to include in the mocks. We're a modern tech consulting firm that drives to interface humanity with technology in a truly cohesive fashion.

```html
<!DOCTYPE html>
<html lang="en">
<head>
<meta charset="utf-8">
<title>Vellum Systemics Business Cards</title>
<link rel="stylesheet" href="https://fonts.googleapis.com/css2?family=Lato:wght@400;700;900&display=swap">
<style>
  :root {
    --backdrop: #1f1f21;
    --brand-blue: #1f7fd0;
    --brand-blue-deep: #1a6fc0;
    --brand-blue-light: #2b8fdb;
    --steel-grey: #8a8c90;
    --ink: #2c2c2e;
    --paper: #ffffff;
  }
  * { box-sizing: border-box; margin: 0; padding: 0; }
  html, body {
    width: 1200px; height: 900px; overflow: hidden;
    background: var(--backdrop);
    font-family: "Lato", sans-serif;
  }
  .card-set {
    position: absolute; inset: 0;
    display: flex; align-items: center; justify-content: center; gap: 40px;
  }
  .card {
    position: relative;
    width: 525px; height: 300px;
    border-radius: 14px;
    overflow: hidden;
  }
  /* Front */
  .card-front {
    background: linear-gradient(160deg, var(--brand-blue-deep) 0%, var(--brand-blue-light) 100%);
    color: var(--paper);
  }
  .front-brand {
    position: absolute; left: 0; right: 0; top: 108px;
    display: flex; align-items: center; justify-content: center; gap: 14px;
  }
  .brand-dot {
    width: 26px; height: 26px; border-radius: 50%;
    background: var(--paper);
  }
  .front-brand .brand-name {
    font-weight: 900; font-size: 42px; letter-spacing: 1px;
  }
  .front-web {
    position: absolute; left: 0; right: 0; bottom: 56px;
    text-align: center;
    font-size: 12px; font-weight: 700; letter-spacing: 4px;
  }
  /* Back */
  .card-back { background: var(--paper); color: var(--ink); }
  .back-swoosh { position: absolute; inset: 0; }
  .back-brand {
    position: absolute; right: 40px; top: 46px;
    display: flex; align-items: center; gap: 10px;
  }
  .back-brand .brand-dot {
    width: 22px; height: 22px; background: var(--brand-blue);
  }
  .back-brand .brand-name {
    font-weight: 900; font-size: 22px; color: var(--brand-blue);
  }
  .holder { position: absolute; left: 34px; top: 96px; }
  .holder-name { font-size: 15px; color: var(--brand-blue); }
  .holder-name strong { font-weight: 700; }
  .holder-title { font-size: 11px; margin-top: 2px; }
  .contact-list {
    position: absolute; left: 50px; bottom: 62px;
    list-style: none; font-size: 12px; line-height: 20px;
  }
  .contact-list li { display: flex; align-items: center; gap: 9px; }
  .contact-icon { width: 12px; height: 12px; fill: var(--brand-blue); flex: none; }
</style>
</head>
<body>
<main class="card-set">
  <section class="card card-front">
    <div class="front-brand">
      <span class="brand-dot"></span>
      <span class="brand-name">Vellum Systemics</span>
    </div>
    <p class="front-web">www.vellumsystemics.com</p>
  </section>

  <section class="card card-back">
    <svg class="back-swoosh" viewBox="0 0 525 300" preserveAspectRatio="none">
      <path d="M0 272 C 180 258, 380 200, 525 118 L 525 300 L 0 300 Z" fill="var(--brand-blue)"/>
      <path d="M205 262 C 330 238, 440 180, 525 104 L 525 114 C 440 186, 335 242, 205 262 Z" fill="var(--steel-grey)"/>
    </svg>
    <div class="back-brand">
      <span class="brand-dot"></span>
      <span class="brand-name">Vellum Systemics</span>
    </div>
    <div class="holder">
      <p class="holder-name">Dana <strong>Whitfield</strong></p>
      <p class="holder-title">Chief Executive Offer</p>
    </div>
    <ul class="contact-list">
      <li>
        <svg class="contact-icon" viewBox="0 0 12 12"><path d="M1 4c0-2 2-3 5-3s5 1 5 3v1H8V4H4v1H1zM3 6h6l2 5H1z"/></svg>
        555.816.4120
      </li>
      <li>
        <svg class="contact-icon" viewBox="0 0 12 12"><path d="M3 1h6v3H3zM1 5h10v4H9v2H3V9H1z"/></svg>
        555.224.3071
      </li>
      <li>
        <svg class="contact-icon" viewBox="0 0 12 12"><path d="M1 2h10v8H1z M1 2l5 4 5-4" stroke="#fff" stroke-width="0.8"/></svg>
        dwhitfield@vellumsystemics.com
      </li>
    </ul>
  </section>
</main>
</body>
</html>
```